Design Card that Captures Life's Moments

Thinking black and white design with maybe some accent colors. Open to others too. Looking for bold and modern to accompany new logo design. For the side without my info, would have tagline of "Capturing Life's Moments" with either logo or website petravossimaging.com. I want the tagline to dominate and be the main focus of that side.

Target Market(s)

Something that can appeal to people who might be interested in family/kids, business, sports, commercial, or birth/newborn photography.

Industry/Entity Type

Professional Photography

Contact Information for Business Card

Font styles to use
Sans Serif
Script
Other font styles liked:
• Go with Logo, but the tagline could be script that popped.

Requirements
Must have
• See details above! Wow factor! Make someone pick my card up and take it home or at least to look at it further.
• Tagline: Capturing Life's Moments (Main text on side without name)
• INFO:
• Petra Voss-Hale - Photographer
• 555-318-0462 - Cell and for SMS
• www.petravossimaging.com - Website (maybe on side with tagline?)
• petra@petrastudioframes.com - Email
Nice to have
• JUST AN IDEA... I would like to see Capturing Life's Moment really take over most of one side of the card. Think greeting card. Where you can't miss it. It is in your face, but nice and elegant. Maybe cursive, but could work with other font. Instead of logo on tagline side, just have petravossimaging.com in smaller text along one of the edges.
Should not have
• Too simple I could of created it, like with only my logo and some typed text.

```html
<!DOCTYPE html>
<html lang="en">
<head>
<meta charset="utf-8">
<title>Petra Voss Imaging – Business Card</title>
<link rel="stylesheet" href="https://fonts.googleapis.com/css2?family=Play:wght@400;700&display=swap">
<style>
  :root {
    --stage: #262427;
    --plum: #3b2a38;
    --coral: #d9534f;
    --ink-dark: #1b1519;
    --ink-mid: #3a3035;
    --white: #ffffff;
    --muted: #bdb3b8;
    --font-text: "Play", sans-serif;
  }
  * { box-sizing: border-box; margin: 0; padding: 0; }
  html, body {
    width: 1200px; height: 900px; overflow: hidden;
    background: var(--stage);
    font-family: var(--font-text);
    color: var(--white);
  }
  .card {
    position: absolute; left: 240px;
    width: 720px; height: 410px;
    background: var(--plum);
    padding: 18px;
  }
  .card--front { top: 35px; }
  .card--back { top: 470px; }
  .card__face { position: relative; width: 684px; height: 374px; overflow: hidden; }
  .block { position: absolute; }

  .camera-shot {
    background: linear-gradient(135deg, var(--ink-dark) 0%, var(--ink-mid) 55%, #241c21 100%);
  }
  .ribbon {
    background: var(--coral);
    clip-path: polygon(0 0, 100% 0, 100% 100%, 14% 100%, 14% 62%, 0 50%);
  }

  /* Front */
  .front__camera { left: 0; top: 0; width: 434px; height: 200px; }
  .front__ribbon { right: 0; top: 0; width: 290px; height: 110px; }
  .front__url {
    position: absolute; right: 16px; top: 12px;
    font-size: 11px; letter-spacing: 0.5px;
  }
  .photo-street { left: 434px; top: 110px; width: 250px; height: 264px;
    background: linear-gradient(160deg, #cfd3c4, #8c7b74 60%, #6b4a45); }
  .photo-wedding { left: 250px; top: 200px; width: 184px; height: 174px;
    background: linear-gradient(170deg, #d8cdbd, #b9a58c 60%, #e8e3da); }
  .photo-party { left: 0; top: 200px; width: 250px; height: 174px;
    background: linear-gradient(120deg, #3d6fd8, #8b3a8f 55%, #d36b8e); }
  .front__message { position: absolute; left: 28px; top: 26px; width: 360px; }
  .front__brand { font-size: 14px; letter-spacing: 3px; text-transform: uppercase; color: var(--muted); }
  .tagline { font-size: 40px; font-weight: 700; line-height: 1.1; margin-top: 14px; }

  /* Back */
  .back__camera { left: 0; top: 0; width: 440px; height: 200px; }
  .back__ribbon { left: 400px; top: 0; width: 284px; height: 145px; }
  .back__brand {
    position: absolute; right: 24px; top: 60px;
    font-size: 20px; font-weight: 400; white-space: nowrap;
  }
  .identity { position: absolute; left: 28px; top: 108px; }
  .identity__name { font-size: 26px; font-weight: 700; }
  .identity__role { font-size: 18px; color: var(--muted); margin-top: 2px; }
  .phone-panel { left: 444px; top: 150px; width: 240px; height: 224px;
    background: var(--coral); text-align: center; padding-top: 40px; }
  .phone-panel__number { font-size: 22px; font-weight: 700; letter-spacing: 1px; margin-top: 14px; }
  .contact-panel { left: 0; top: 205px; width: 439px; height: 169px;
    background: var(--coral); padding: 18px 0 0 110px; }
  .contact-panel__icon { display: block; margin-left: 70px; }
  .contact-panel__line { font-size: 19px; font-weight: 700; letter-spacing: 0.5px; margin-top: 4px; white-space: nowrap; }
  .contact-panel__line:first-of-type { margin-top: 14px; }
</style>
</head>
<body>

<section class="card card--front" aria-label="Card front">
  <div class="card__face">
    <div class="block camera-shot front__camera" role="img" aria-label="Dark close-up photograph of a camera"></div>
    <div class="block ribbon front__ribbon">
      <span class="front__url">www.petravossimaging.com</span>
    </div>
    <div class="block photo-street" role="img" aria-label="Photograph of a couple walking on a city street"></div>
    <div class="block photo-wedding" role="img" aria-label="Wedding photograph of a bride and groom"></div>
    <div class="block photo-party" role="img" aria-label="Photograph of friends at a colourful party"></div>
    <div class="front__message">
      <p class="front__brand">Petra Voss Imaging</p>
      <p class="tagline">Capturing Life's<br>Moments</p>
    </div>
  </div>
</section>

<section class="card card--back" aria-label="Card back">
  <div class="card__face">
    <div class="block camera-shot back__camera" role="img" aria-label="Dark close-up photograph of a camera"></div>
    <div class="identity">
      <p class="identity__name">Petra Voss-Hale</p>
      <p class="identity__role">Photographer</p>
    </div>
    <div class="block ribbon back__ribbon">
      <p class="back__brand">Petra Voss Imaging</p>
    </div>
    <div class="block phone-panel">
      <svg class="phone-panel__icon" width="110" height="72" viewBox="0 0 110 72" aria-hidden="true">
        <path d="M8 24 Q8 6 55 6 Q102 6 102 24 L102 30 L80 30 L80 20 Q55 14 30 20 L30 30 L8 30 Z" fill="var(--white)"/>
        <path d="M30 32 L80 32 L94 68 L16 68 Z" fill="var(--white)"/>
        <circle cx="55" cy="50" r="12" fill="var(--coral)"/>
        <circle cx="55" cy="50" r="6" fill="var(--white)"/>
      </svg>
      <p class="phone-panel__number">555-318-0462</p>
    </div>
    <div class="block contact-panel">
      <svg class="contact-panel__icon" width="60" height="60" viewBox="0 0 60 60" aria-hidden="true">
        <g fill="none" stroke="var(--white)" stroke-width="4">
          <circle cx="30" cy="30" r="26"/>
          <ellipse cx="30" cy="30" rx="12" ry="26"/>
          <line x1="4" y1="30" x2="56" y2="30"/>
          <path d="M9 17 H51 M9 43 H51"/>
        </g>
      </svg>
      <p class="contact-panel__line">petra@petrastudioframes.com</p>
      <p class="contact-panel__line">www.petravossimaging.com</p>
    </div>
  </div>
</section>

</body>
</html>
```